Icon-Design für App
Zielgruppe
quobarin.com is an app for more social closeness: You can scan people around you (50m) and give quobarins (nobody can see your likes unless you like each other). It's a kind of the opposite of Flurma: Meet first live in a bar, during shopping at the bus-station.... and use the app just as an 'ice-breaker'. Therefore the scanner of quobarin.com is very accurate (50m) and realtime....which is so far unique. We got more than 1000 Users within the first weeks after launch...and it's time to style the app as many people said it looks terrible.... Quobarin is available on appvelo depot or just as a web app in every browser over www.quobarin.com.
Aufgabenstellung
we got many feedbacks that the app-function is great but the design looks terrible. Can you change this? If you tested the app (www.quobarin.com) and once you understood the idea: feel free to follow your feelings when re-designing! We are open to all changes. I actually would like to keep the main logo, the 'shy smiling heart with the hand in front of mouth'...but if you have a better Idea...just do it!

```html
<!DOCTYPE html>
<html lang="en">
<head>
<meta charset="utf-8">
<title>Quobarin – Nearby</title>
<link rel="stylesheet" href="https://fonts.googleapis.com/css2?family=Roboto:wght@400;500;700&display=swap">
<style>
  :root{
    --page:#eeeeef;
    --screen:#f4f5f7;
    --orange-top:#f38b0e;
    --orange:#f25c05;
    --pill:#f0583a;
    --yellow:#ffc000;
    --olive:#7a5800;
    --rust:#a83a0a;
    --mute-tile:#c9c9c9;
    --mute-icon:#9b9b9b;
    --grey-tile:#8b8b8b;
    --ink:#2b2b2b;
    --white:#ffffff;
    --row-line:#e3e4e7;
  }
  *{box-sizing:border-box;margin:0;padding:0}
  html,body{width:1200px;height:960px;overflow:hidden}
  body{background:var(--page);font-family:"Roboto",Arial,sans-serif;position:relative}

  .screen{position:absolute;left:390px;top:32px;width:420px;height:896px;border-radius:44px;
    background:var(--screen);overflow:hidden;box-shadow:0 10px 30px rgba(0,0,0,.12)}

  .header-bg{position:absolute;left:0;top:0}
  .status-time{position:absolute;left:40px;top:19px;font-size:12px;font-weight:700;color:var(--ink)}
  .status-icons{position:absolute;right:26px;top:19px}
  .icon-logout,.icon-help{position:absolute;top:48px;width:34px;height:34px}
  .icon-logout{left:22px}
  .icon-help{right:22px}
  .profile-photo{position:absolute;left:160px;top:55px;width:100px;height:100px;border-radius:50%;
    border:3px solid var(--white);background:radial-gradient(circle at 50% 60%,#c89a7a 0 30%,#6f8fe0 31% 100%)}
  .brand-name{position:absolute;left:0;width:420px;top:163px;text-align:center;color:var(--white);
    font-size:21px;font-weight:500;letter-spacing:3px}

  .person-row{position:absolute;left:10px;width:404px;height:90px;background:var(--white);
    border:1px solid var(--row-line);border-radius:14px;overflow:hidden}
  .person-photo{position:absolute;left:12px;top:10px;width:70px;height:70px;border-radius:50%;border:2px solid #fff;
    box-shadow:0 0 0 1px #ddd}
  .distance-pill{position:absolute;left:93px;top:28px;width:90px;height:34px;border-radius:17px;background:var(--pill);
    color:var(--white);font-size:13px;font-weight:500;line-height:34px;text-align:center}
  .distance-pill::before{content:"";position:absolute;left:-6px;top:15px;border:7px solid transparent;
    border-right:9px solid var(--pill);border-left:0;transform:rotate(-25deg)}
  .chat-tile,.like-tile{position:absolute;top:0;height:100%;display:flex;align-items:center;justify-content:center}
  .chat-tile{left:235px;width:87px}
  .like-tile{left:322px;width:82px}
  .chat-tile svg{width:48px;height:44px}
  .like-tile svg{width:52px;height:52px}
  .logo-dot{width:46px;height:46px;border-radius:50%}

  .tile-muted{background:var(--mute-tile);color:var(--mute-icon)}
  .tile-yellow{background:var(--yellow);color:var(--white)}
  .tile-rust{background:var(--rust);color:var(--white)}
  .tile-orange{background:var(--orange);color:var(--white)}
  .tile-olive{background:var(--olive)}
  .tile-grey{background:var(--grey-tile)}

  .tab-bar{position:absolute;left:0;bottom:0;width:420px;height:86px;background:var(--white)}
  .tab{position:absolute;top:58px;font-size:15px;font-weight:500;color:var(--ink);text-align:center}
  .tab-friends{left:36px;width:70px}
  .tab-community{left:300px;width:100px}
  .tab-scan{left:140px;width:124px;color:var(--orange);letter-spacing:1.5px;font-weight:700}
  .tab-icon{position:absolute;top:12px}
  .badge{position:absolute;left:84px;top:10px;width:22px;height:22px;border-radius:50%;background:#f0452a;
    color:#fff;font-size:13px;font-weight:700;line-height:22px;text-align:center;border:2px solid #fff}
  .scan-button{position:absolute;left:158px;top:-44px;width:88px;height:88px;border-radius:50%;
    background:var(--orange);box-shadow:0 0 0 6px rgba(242,92,5,.25);display:flex;align-items:center;justify-content:center}
  .scan-button svg{width:44px;height:44px}
  .home-indicator{position:absolute;left:142px;bottom:6px;width:120px;height:4px;border-radius:2px;background:#9a9a9a}
</style>
</head>
<body>
<svg width="0" height="0" style="position:absolute">
  <symbol id="chat" viewBox="0 0 48 44">
    <path d="M14 10h28a4 4 0 0 1 4 4v16a4 4 0 0 1-4 4h-2v7l-7-7H14a4 4 0 0 1-4-4V14a4 4 0 0 1 4-4z" fill="none" stroke="currentColor" stroke-width="3"/>
    <path d="M6 2h28a4 4 0 0 1 4 4v18a4 4 0 0 1-4 4H14l-6 6v-6H6a4 4 0 0 1-4-4V6a4 4 0 0 1 4-4z" fill="currentColor"/>
    <path d="M9 10h20M9 16h24M9 22h14" stroke="#fff" stroke-width="3" opacity=".85"/>
  </symbol>
  <symbol id="heart" viewBox="0 0 24 24">
    <path d="M12 21s-7.5-4.6-10-9.3C.3 8.3 2.3 4 6.3 4c2.3 0 4 1.3 5.7 3.3C13.7 5.3 15.4 4 17.7 4c4 0 6 4.3 4.3 7.7C19.5 16.4 12 21 12 21z" fill="currentColor"/>
  </symbol>
</svg>

<main class="screen">
  <svg class="header-bg" width="420" height="215" viewBox="0 0 420 215">
    <defs><linearGradient id="hg" x1="0" y1="0" x2="0" y2="1"><stop offset="0" stop-color="#f38b0e"/><stop offset="1" stop-color="#f05a05"/></linearGradient></defs>
    <path d="M0 0H420V140Q210 286 0 140Z" fill="url(#hg)"/>
  </svg>
  <div class="status-time">9:41</div>
  <svg class="status-icons" width="62" height="12" viewBox="0 0 62 12">
    <rect x="0" y="8" width="3" height="4" fill="#222"/><rect x="5" y="5" width="3" height="7" fill="#222"/><rect x="10" y="2" width="3" height="10" fill="#222"/>
    <path d="M22 5a9 9 0 0 1 12 0M25 8a5 5 0 0 1 6 0" stroke="#222" stroke-width="2" fill="none"/><circle cx="28" cy="11" r="1.3" fill="#222"/>
    <rect x="42" y="2" width="17" height="9" rx="2" fill="#222"/><rect x="60" y="5" width="2" height="3" fill="#222"/>
  </svg>
  <svg class="icon-logout" viewBox="0 0 34 34" fill="none" stroke="#fff" stroke-width="2.4">
    <path d="M16 5H5v24h11"/><path d="M31 17H13M20 10l-7 7 7 7"/>
  </svg>
  <svg class="icon-help" viewBox="0 0 34 34" fill="none" stroke="#fff" stroke-width="2.2">
    <circle cx="17" cy="17" r="14"/><path d="M12.5 13a4.5 4.5 0 1 1 6 4.2c-1.2.5-1.5 1.3-1.5 2.8"/><circle cx="17" cy="24.5" r="1" fill="#fff"/>
  </svg>
  <div class="profile-photo" role="img" aria-label="Profile photo of the signed-in user"></div>
  <div class="brand-name">Quobarin</div>

  <section class="person-row" style="top:262px">
    <div class="person-photo" role="img" aria-label="Profile photo of a nearby user" style="background:radial-gradient(circle at 50% 55%,#d7a48a 0 30%,#2a2220 31% 60%,#9aab6a 61%)"></div>
    <span class="distance-pill">New 50m</span>
    <div class="chat-tile tile-muted"><svg><use href="#chat"/></svg></div>
    <div class="like-tile tile-olive"><span class="logo-dot" style="background:#ffc400"></span></div>
  </section>

  <section class="person-row" style="top:363px">
    <div class="person-photo" role="img" aria-label="Profile photo of a nearby user" style="background:radial-gradient(circle at 50% 55%,#c08a6c 0 30%,#1d2c52 31%)"></div>
    <span class="distance-pill">New 50m</span>
    <div class="chat-tile tile-yellow"><svg><use href="#chat"/></svg></div>
    <div class="like-tile tile-orange"><svg><use href="#heart"/></svg></div>
  </section>

  <section class="person-row" style="top:464px">
    <div class="person-photo" role="img" aria-label="Profile photo of a nearby user" style="background:radial-gradient(circle at 50% 55%,#b9b9b9 0 30%,#1a1a1a 31%)"></div>
    <span class="distance-pill">New 50m</span>
    <div class="chat-tile tile-rust">
      <svg viewBox="0 0 48 44"><path d="M14 10h28a4 4 0 0 1 4 4v16a4 4 0 0 1-4 4h-2v7l-7-7H14a4 4 0 0 1-4-4V14a4 4 0 0 1 4-4z" fill="none" stroke="#fff" stroke-width="3"/><rect x="0" y="2" width="38" height="24" rx="4" fill="#fff"/><path d="M10 26l-4 7 10-7z" fill="#fff"/><text x="19" y="20" text-anchor="middle" font-family="Roboto,Arial,sans-serif" font-weight="700" font-size="13" fill="#a83a0a">NEW</text></svg>
    </div>
    <div class="like-tile tile-orange"><svg><use href="#heart"/></svg></div>
  </section>

  <section class="person-row" style="top:565px">
    <div class="person-photo" role="img" aria-label="Profile photo of a nearby user" style="background:radial-gradient(circle at 50% 55%,#d9a488 0 30%,#5a3324 31% 60%,#8a6a56 61%)"></div>
    <span class="distance-pill">New 50m</span>
    <div class="chat-tile tile-yellow"><svg><use href="#chat"/></svg></div>
    <div class="like-tile tile-grey"><span class="logo-dot" style="background:#dcdcdc"></span></div>
  </section>

  <section class="person-row" style="top:666px">
    <div class="person-photo" role="img" aria-label="Profile photo of a nearby user" style="background:radial-gradient(circle at 50% 55%,#e0b7a4 0 30%,#3b2a26 31% 60%,#c9c4c2 61%)"></div>
    <span class="distance-pill">New 50m</span>
    <div class="chat-tile tile-muted"><svg><use href="#chat"/></svg></div>
    <div class="like-tile tile-olive"><span class="logo-dot" style="background:#ffc400"></span></div>
  </section>

  <section class="person-row" style="top:767px">
    <div class="person-photo" role="img" aria-label="Profile photo of a nearby user" style="background:radial-gradient(circle at 50% 55%,#b07f62 0 30%,#1e2a44 31%)"></div>
    <span class="distance-pill">New 50m</span>
    <div class="chat-tile tile-yellow"><svg><use href="#chat"/></svg></div>
    <div class="like-tile tile-orange"><svg><use href="#heart"/></svg></div>
  </section>

  <nav class="tab-bar">
    <svg class="tab-icon" style="left:48px" width="42" height="32" viewBox="0 0 42 32" fill="#333">
      <circle cx="24" cy="8" r="6"/><path d="M12 30c0-8 5-12 12-12s12 4 12 12z"/>
      <circle cx="11" cy="11" r="5"/><path d="M0 30c0-7 4-10 10-10 2 0 3 .3 4 .8-2 2-3 5-3 9.2z"/>
    </svg>
    <span class="badge">1</span>
    <span class="tab tab-friends">Friends</span>

    <div class="scan-button"><svg style="color:#fff"><use href="#heart"/></svg></div>
    <span class="tab tab-scan">Scan 50 m</span>

    <svg class="tab-icon" style="left:333px" width="34" height="34" viewBox="0 0 34 34">
      <circle cx="17" cy="17" r="15" fill="#333"/>
      <path d="M9 8c3 1 4 4 7 4s3 4 0 6-2 6-4 8c-2-3-1-6-3-8S5 12 9 8zM22 6c2 2 6 4 7 9-2 0-4-1-5 1s-4-2-3-4 0-4 1-6zM23 22c2-1 4 0 5 1-1 3-3 5-6 6 0-3-1-5 1-7z" fill="#fff"/>
    </svg>
    <span class="tab tab-community">Community</span>
    <div class="home-indicator"></div>
  </nav>
</main>
</body>
</html>
```